Conference banner for Beacon training organisation

We empower everyday heroes.
We provide training that empowers individuals to create positive change in themselves, their community, and the world.
We need a large banner design to promote the organisation at conferences and events. We are open to ideas and creativity.
It may involve creatively displaying our logo only, or it may involve our logo and a summary of our products (Beacon training, Steady Minds Crisis Care).
Size: 820mm width x 1790mm height
300dpi
Target Market(s)
Educators and frontline health, community, and social workers.
Industry/Entity Type
Training
Colors
Designer to choose colors to be used in the design.

```html
<!DOCTYPE html>
<html lang="en">
<head>
<meta charset="utf-8">
<title>Lumen Street – Conference Banner</title>
<link rel="stylesheet" href="https://fonts.googleapis.com/css2?family=Montserrat:wght@600;700&display=swap">
<style>
  :root {
    --backdrop: #6e6e6e;
    --paper: #ffffff;
    --brand-blue: #3a59b2;
    --brand-red: #ae3549;
    --ring-grey: #e4e4e4;
    --url-border: rgba(255,255,255,0.75);
  }
  * { margin: 0; padding: 0; box-sizing: border-box; }
  html, body {
    width: 1200px; height: 2315px; overflow: hidden;
    background: var(--backdrop);
    font-family: "Montserrat", Arial, sans-serif;
  }
  .banner {
    position: absolute; left: 129px; top: 129px;
    width: 942px; height: 2057px;
    background: var(--paper); overflow: hidden;
  }
  .banner__band { position: absolute; left: 0; top: 0; width: 942px; height: 2057px; }
  .brand-mark {
    position: absolute; left: 361px; top: 130px;
    width: 220px; height: 220px; border-radius: 50%;
    background: var(--brand-blue);
  }
  .brand-name {
    position: absolute; left: 0; width: 100%; top: 420px;
    text-align: center; color: var(--brand-blue); white-space: nowrap;
    font-weight: 600; font-size: 86px; letter-spacing: 3px; line-height: 1;
  }
  .headline {
    position: absolute; left: 0; width: 100%; top: 654px;
    text-align: center; color: var(--brand-red);
    font-weight: 700; font-size: 92px; line-height: 116px; letter-spacing: 1px;
  }
  .product { position: absolute; width: 420px; text-align: center; }
  .product__badge {
    display: block; margin: 0 auto;
    width: 282px; height: 282px; border-radius: 50%;
    background: var(--ring-grey);
    padding: 21px;
  }
  .product__icon {
    display: block; width: 240px; height: 240px; border-radius: 50%;
    background: var(--brand-red);
  }
  .product__label {
    color: var(--paper); font-weight: 700; font-size: 35px; line-height: 46px;
    margin-top: 30px; white-space: nowrap;
  }
  .product--beacon { left: 62px; top: 1289px; }
  .product--steady { left: 458px; top: 1231px; }
  .product--steady .product__label { margin-top: 38px; }
  .web-address {
    position: absolute; left: 87px; top: 1835px;
    width: 768px; height: 87px;
    border: 2px solid var(--url-border);
    color: var(--paper); font-weight: 700; font-size: 38px; white-space: nowrap;
    display: flex; align-items: center; justify-content: center;
  }
</style>
</head>
<body>
  <main class="banner">
    <svg class="banner__band" viewBox="0 0 942 2057" aria-hidden="true">
      <polygon points="300,1451 942,1337 942,1366 0,1501 0,1504" fill="var(--brand-red)"/>
      <polygon points="0,1501 942,1366 942,2057 0,2057" fill="var(--brand-blue)"/>
    </svg>

    <span class="brand-mark" aria-hidden="true"></span>
    <h1 class="brand-name">LUMEN STREET</h1>

    <p class="headline">WE<br>EMPOWER<br>EVERYDAY<br>HEROES</p>

    <section class="product product--beacon">
      <span class="product__badge"><span class="product__icon" role="img" aria-label="Icon of a standing caped figure"></span></span>
      <p class="product__label">BEACON TRAINING</p>
    </section>

    <section class="product product--steady">
      <span class="product__badge"><span class="product__icon" role="img" aria-label="Icon of a head with a magnifying glass"></span></span>
      <p class="product__label">STEADY MINDS<br>CRISIS CARE</p>
    </section>

    <p class="web-address">www.lumenstreetlearning.com.au</p>
  </main>
</body>
</html>
```